Creative/innovative law firm website

A law firm website that immediately looks different from other law firm websites. We like the color scheme (dark background with warm, neutral colors) and simple, organic logos (trees, leaves, etc.) of this website: https://brambleworth.legal/

We'll be offering creative/innovative solutions to complex problems faced by state governments, industries, other law firms, and individuals. We're located in Montana (U.S.A.), and the outdoors is a huge part of our lives and identities.

We will need a home page, an "About Us" page with a separate subpage for each attorney (two attorneys), a blog or "Publications" page, a payment portal (which will integrate with Quillo), and a "Services" page.

```html
<!DOCTYPE html>
<html lang="en">
<head>
<meta charset="utf-8">
<title>Hartwell &amp; Brody P.C.</title>
<link href="https://fonts.googleapis.com/css2?family=Libre+Baskerville:wght@400;700&family=Poppins:wght@400;500;600&display=swap" rel="stylesheet">
<style>
:root{
  --rust:#c4620c;
  --rust-dark:#a04f08;
  --ink:#111010;
  --ink-soft:#1d1a18;
  --cream:#f8f5ef;
  --text:#2a2a2a;
  --muted:#6d6d6d;
  --white:#ffffff;
}
*{margin:0;padding:0;box-sizing:border-box}
html,body{width:1200px;height:4967px;overflow:hidden}
body{position:relative;background:var(--white);font-family:"Poppins",sans-serif;color:var(--text)}
.serif{font-family:"Libre Baskerville",serif}
.abs{position:absolute}
.photo{position:absolute}
.btn{position:absolute;background:var(--rust);color:var(--white);font-family:"Libre Baskerville",serif;font-weight:700;font-size:12px;letter-spacing:.5px;display:flex;align-items:center;justify-content:center;box-shadow:4px 4px 0 -1px var(--white),5px 5px 0 0 var(--rust)}
.eyebrow{position:absolute;font-size:13px;font-weight:500;display:flex;align-items:center;gap:12px;text-transform:uppercase;letter-spacing:.3px}
.eyebrow::before,.eyebrow::after{content:"";width:48px;height:1px;background:currentColor;opacity:.6}
.heading{position:absolute;font-family:"Libre Baskerville",serif;font-weight:700;color:var(--rust);font-size:29px}

/* hero */
.hero{position:absolute;left:0;top:0;width:1200px;height:675px;clip-path:polygon(0 0,100% 0,100% 675px,0 608px);background:linear-gradient(100deg,#161311 0%,#2a231e 40%,#3f3630 60%,#1b1816 100%)}
.topbar{position:absolute;top:0;left:0;width:1200px;height:38px;background:rgba(0,0,0,.75);color:var(--white);font-size:12px}
.topbar .item{position:absolute;top:11px;display:flex;align-items:center;gap:10px}
.topbar .cta{position:absolute;right:60px;top:0;width:165px;height:38px;background:var(--rust);font-family:"Libre Baskerville",serif;font-weight:700;font-size:11px;display:flex;align-items:center;justify-content:center}
.logo{position:absolute;font-family:"Libre Baskerville",serif;font-weight:700;font-size:27px;line-height:36px}
.logo .l1{color:var(--white)}
.logo .l2{color:var(--rust);padding-left:34px;display:block}
.nav{position:absolute;top:68px;color:var(--white);font-family:"Libre Baskerville",serif;font-size:13px}
.nav a{position:absolute;white-space:nowrap;color:inherit;text-decoration:none}
.nav a.active{color:var(--rust)}
.hero-title{position:absolute;left:62px;top:218px;font-family:"Libre Baskerville",serif;font-weight:700;font-size:64px;line-height:76px;color:var(--white)}
.hero-text{position:absolute;left:62px;top:380px;width:430px;font-size:12px;line-height:19px;color:var(--white)}

/* about */
.about-text .lead{position:absolute;left:189px;top:832px;width:530px;font-family:"Libre Baskerville",serif;font-size:14.5px;line-height:26px;color:var(--ink)}
.about-text .body{position:absolute;left:189px;top:902px;width:420px;font-size:12px;line-height:20px;color:var(--muted)}
.features{position:absolute;left:0;top:1085px;width:1200px;height:330px;background:var(--cream);clip-path:polygon(0 0,100% 0,100% 100%,0 310px)}
.feature{position:absolute;top:1145px;width:200px}
.feature h3{font-family:"Libre Baskerville",serif;font-weight:400;font-size:19px;color:var(--ink);margin-top:14px}
.feature p{font-size:12px;line-height:20px;color:var(--muted);margin-top:10px;width:185px}

/* services */
.services{position:absolute;left:0;top:1390px;width:1200px;height:810px;background:linear-gradient(90deg,#0e0d0c,#1c1a18 50%,#2a2826);clip-path:polygon(0 0,100% 85px,100% 730px,0 800px)}
.stat{position:absolute;top:1608px;width:200px;text-align:center;color:var(--white)}
.stat b{display:block;font-family:"Libre Baskerville",serif;font-weight:700;font-size:34px}
.stat span{display:block;font-family:"Libre Baskerville",serif;font-size:14px;margin-top:10px}
.svc{position:absolute;width:232px;height:188px;background:rgba(88,52,18,.72);color:var(--white);text-align:center;padding-top:14px}
.svc.boxed{border:1.5px solid #e9e1d8;border-radius:6px;background:rgba(70,44,20,.65)}
.svc h4{font-family:"Libre Baskerville",serif;font-weight:400;font-size:16px;margin-top:8px}
.svc p{font-size:12px;line-height:20px;margin:10px auto 0;width:190px}

/* appointment */
.quote{position:absolute;left:97px;width:310px;font-size:12px;line-height:20px;color:var(--muted)}
.quote .mark{position:absolute;left:-2px;top:-14px;font-family:"Libre Baskerville",serif;font-size:44px;color:var(--rust);opacity:.35}
.client{position:absolute;left:97px;display:flex;gap:20px;align-items:center}
.avatar{width:46px;height:46px;border-radius:50%;background:linear-gradient(135deg,#9aa3ad,#3d4652)}
.client b{display:block;font-family:"Libre Baskerville",serif;font-size:13px;color:var(--ink)}
.client span{font-size:11px;color:var(--muted)}
.form{position:absolute;left:556px;top:2934px;width:525px;height:444px;background:linear-gradient(135deg,#141312,#232120)}
.form h3{position:absolute;left:42px;top:70px;font-family:"Libre Baskerville",serif;font-weight:700;font-size:26px;color:var(--white)}
.field{position:absolute;height:36px;background:#3a3837;color:#d9d9d9;font-size:11px;padding:10px 17px}

/* news */
.news{position:absolute;left:0;top:3410px;width:1200px;height:620px;background:linear-gradient(90deg,#0f0e0d,#1e1b19 50%,#0f0e0d);clip-path:polygon(0 0,100% 40px,100% 560px,0 620px)}
.card{position:absolute;top:3621px;width:296px;height:355px;background:var(--white);box-shadow:0 4px 14px rgba(0,0,0,.15)}
.card .img{position:absolute;left:8px;top:8px;width:280px;height:240px}
.card .meta{position:absolute;left:14px;top:260px;font-size:11px;color:var(--muted);display:flex;gap:40px}
.card .meta span{display:flex;gap:8px;align-items:center}
.card h4{position:absolute;left:16px;top:292px;width:270px;font-family:"Libre Baskerville",serif;font-weight:400;font-size:15px;line-height:27px;color:var(--ink)}

/* clients */
.brand{position:absolute;top:4153px;width:208px;height:85px;background:var(--white);border:1px solid #dcdcdc;box-shadow:0 2px 6px rgba(0,0,0,.08);display:flex;align-items:center;justify-content:center;gap:10px;font-family:"Poppins",sans-serif;font-weight:500;font-size:28px;color:#2a2a2a}
.brand i{width:22px;height:22px;background:#2a2a2a;border-radius:50%;display:block}

/* footer */
.footer{position:absolute;left:0;top:4460px;width:1200px;height:507px;background:linear-gradient(90deg,#0f0e0d,#1c1a18 60%,#0f0e0d)}
.fcol{position:absolute;top:4683px;color:#d8d8d8;font-size:12px}
.fcol h5{font-family:"Libre Baskerville",serif;font-weight:400;font-size:18px;color:var(--rust);margin-bottom:14px}
.fcol li{list-style:none;line-height:30px}
.copy{position:absolute;left:0;top:4933px;width:1200px;height:34px;background:var(--rust);color:var(--white);font-size:11px;display:flex;align-items:center;justify-content:center}
</style>
</head>
<body>

<!-- HERO -->
<section class="hero">
  <div class="photo" role="img" aria-label="Photo of a young attorney in a suit signing documents at a desk with a gavel" style="left:0;top:0;width:1200px;height:675px;background:radial-gradient(ellipse at 62% 45%,rgba(120,100,85,.55),rgba(0,0,0,0) 55%)"></div>
</section>
<div class="topbar">
  <div class="item" style="left:58px"><svg width="14" height="14" viewBox="0 0 24 24" fill="none" stroke="#c4620c" stroke-width="2"><path d="M5 3h4l2 5-3 2a12 12 0 0 0 6 6l2-3 5 2v4a2 2 0 0 1-2 2A17 17 0 0 1 3 5a2 2 0 0 1 2-2z"/></svg>+ 1-406-555-0142</div>
  <div class="item" style="left:250px"><svg width="22" height="14" viewBox="0 0 22 14" fill="none" stroke="#c4620c" stroke-width="1.6"><rect x="1" y="1" width="20" height="12"/><path d="M1 1l10 7 10-7"/></svg>hello@hartwellbrody.law</div>
  <div class="item" style="left:556px"><svg width="16" height="16" viewBox="0 0 24 24" fill="none" stroke="#c4620c" stroke-width="2"><circle cx="12" cy="12" r="10"/><path d="M12 6v6l4 2"/></svg>Mon - Frid 9:00 -17:00</div>
  <div class="cta">FREE CONSULTATION</div>
</div>
<div class="logo" style="left:62px;top:48px"><span class="l1">Hartwell &amp;</span><span class="l2">Brody P.C.</span></div>
<nav class="nav">
  <a class="active" style="left:639px">Home</a>
  <a style="left:706px">About Us</a>
  <a style="left:795px">Services</a>
  <a style="left:878px">Payment</a>
  <a style="left:965px">Attorney</a>
  <a style="left:1047px">Blog</a>
</nav>
<svg class="abs" style="left:1106px;top:61px" width="34" height="34" viewBox="0 0 34 34" fill="none" stroke="#c4620c" stroke-width="1.6"><circle cx="17" cy="17" r="15.5"/><circle cx="16" cy="16" r="5"/><path d="M20 20l4 4"/></svg>
<h1 class="hero-title">Hartwell &amp;<br>Brody P.C.</h1>
<p class="hero-text">It is a long established fact that a reader will be distracted by the readable content of a page when looking at its layout.</p>
<div class="btn" style="left:62px;top:436px;width:126px;height:37px">READ MORE</div>

<!-- ABOUT -->
<section class="features"></section>
<div class="abs" style="left:965px;top:1010px;width:235px;height:150px;background:var(--rust)"></div>
<div class="photo" role="img" aria-label="Photo of two attorneys reviewing documents in an office with a flag" style="left:727px;top:755px;width:450px;height:358px;background:linear-gradient(135deg,#3b352f,#6e6258 50%,#2b2622)"></div>
<div class="eyebrow" style="left:207px;top:746px;color:var(--ink)">Welcome to</div>
<h2 class="heading" style="left:189px;top:778px">About Hartwell &amp; Brody P.C.</h2>
<div class="about-text">
  <p class="lead">Lorem Ipsum is simply dummy text of the printing and<br>typesetting industry. Lorem Ipsum has been the industry's</p>
  <p class="body">It is a long established fact that a reader will be distracted by the readable content of a page when looking at its layout. The point of using Lorem Ipsum is that it has a more-or-less normal distribution of letters, as opposed to using 'Content here, content here', making it look like readable English.</p>
</div>
<div class="btn" style="left:189px;top:1019px;width:124px;height:35px">READ MORE</div>

<div class="feature" style="left:189px">
  <svg width="60" height="52" viewBox="0 0 60 52" fill="none" stroke="#c4620c" stroke-width="1.8"><circle cx="22" cy="24" r="20" fill="#f1e4d6" stroke="none"/><circle cx="33" cy="12" r="6"/><path d="M23 34v-6a10 10 0 0 1 20 0v6"/><path d="M14 46l3-6 3 6-5-3h6zM30 46l3-6 3 6-5-3h6zM46 46l3-6 3 6-5-3h6z"/></svg>
  <h3>Experience</h3>
  <p>Lorem Ipsum is simply dummy text of the printing and typesetting industry. Lorem Ipsum has been the industry's</p>
</div>
<div class="feature" style="left:428px">
  <svg width="60" height="52" viewBox="0 0 60 52" fill="none" stroke="#c4620c" stroke-width="1.8"><circle cx="20" cy="26" r="20" fill="#f1e4d6" stroke="none"/><path d="M10 20h10v-4a4 4 0 0 1 8 0v4h10v10h-4a4 4 0 0 0 0 8h4v10H10z"/><path d="M38 4h14v14H38z"/></svg>
  <h3>Effective</h3>
  <p>Lorem Ipsum is simply dummy text of the printing and typesetting industry. Lorem Ipsum has been the industry's</p>
</div>
<div class="feature" style="left:691px">
  <svg width="60" height="52" viewBox="0 0 60 52" fill="none" stroke="#c4620c" stroke-width="1.8"><circle cx="22" cy="28" r="20" fill="#f1e4d6" stroke="none"/><path d="M36 8c-3-5-11-3-10 4 1 5 10 10 10 10s9-5 10-10c1-7-7-9-10-4z"/><path d="M6 34l10-6h12l-10 6h12l12-8 4 4-16 12H14l-8 2"/></svg>
  <h3>Here For You</h3>
  <p>Lorem Ipsum is simply dummy text of the printing and typesetting industry. Lorem Ipsum has been the industry's</p>
</div>

<!-- SERVICES -->
<section class="services"></section>
<div class="eyebrow" style="left:518px;top:1528px;color:#fff">Practice Area</div>
<h2 class="heading" style="left:0;width:1292px;text-align:center;top:1558px">Our Services</h2>
<div class="stat" style="left:136px"><b>200+</b><span>Completed Works</span></div>
<div class="stat" style="left:389px"><b style="color:var(--rust)">3210 +</b><span>Contract Signed</span></div>
<div class="stat" style="left:638px"><b>250+</b><span>Registered Cases</span></div>
<div class="stat" style="left:865px"><b>100%</b><span>Trusted Clients</span></div>
<div class="photo" role="img" aria-label="Photo of a lawyer in a robe reading a book beside shelves of law volumes" style="left:150px;top:1720px;width:375px;height:397px;background:linear-gradient(90deg,#a8601e,#d9a25e 35%,#e8e2da 50%,#2a2522 75%,#d8d3cc)"></div>
<div class="svc boxed" style="left:562px;top:1720px">
  <svg width="56" height="46" viewBox="0 0 56 46" fill="none" stroke="#fff" stroke-width="1.6"><path d="M28 2v6M22 14a6 6 0 0 1 12 0M8 22l20-8 20 8zM10 24v16M18 24v16M26 24v16M30 24v16M38 24v16M46 24v16M4 42h48M6 45h44"/></svg>
  <h4>State governments</h4>
  <p>Lorem Ipsum is simply dummy text of the printing and typesetting .</p>
</div>
<div class="svc" style="left:818px;top:1720px">
  <svg width="56" height="46" viewBox="0 0 56 46" fill="none" stroke="#fff" stroke-width="1.6"><path d="M6 44V22l12 6v-6l12 6v-6l12 6V4h6v40zM4 44h48M20 10a4 4 0 0 1 8 0M36 4a4 4 0 0 1 6-2"/><path d="M12 34h4M22 34h4M32 34h4"/></svg>
  <h4>Industries</h4>
  <p>Lorem Ipsum is simply dummy text of the printing and typesetting .</p>
</div>
<div class="svc" style="left:562px;top:1929px">
  <svg width="56" height="46" viewBox="0 0 56 46" fill="none" stroke="#fff" stroke-width="1.6"><path d="M6 14L28 3l22 11zM8 16h40M12 18v18M20 18v18M28 18v18M36 18v18M44 18v18M6 38h44M4 43h48"/></svg>
  <h4>Law firms</h4>
  <p>Lorem Ipsum is simply dummy text of the printing and typesetting .</p>
</div>
<div class="svc" style="left:818px;top:1929px">
  <svg width="56" height="46" viewBox="0 0 56 46" fill="none" stroke="#fff" stroke-width="1.6"><circle cx="28" cy="12" r="9"/><path d="M10 45V34a10 10 0 0 1 10-10h16a10 10 0 0 1 10 10v11M24 24l4 10 4-10M28 34v11"/></svg>
  <h4>Individuals</h4>
  <p>Lorem Ipsum is simply dummy text of the printing and typesetting .</p>
</div>

<!-- CASE STUDIES -->
<div class="eyebrow" style="left:258px;top:2290px;color:var(--ink)">What We</div>
<h2 class="heading" style="left:241px;top:2330px">Case Studies</h2>
<div class="photo" role="img" aria-label="Photo of a gavel on a desk" style="left:195px;top:2410px;width:240px;height:302px;background:linear-gradient(135deg,#e6e6e4,#bcbcb8 60%,#5a5855)"></div>
<div class="photo" role="img" aria-label="Photo of two colleagues reviewing a folder together" style="left:442px;top:2374px;width:263px;height:374px;background:linear-gradient(135deg,#3a3c40,#8c8d90 50%,#2e3034)"></div>
<div class="photo" role="img" aria-label="Photo of hands exchanging a tablet over documents" style="left:712px;top:2410px;width:240px;height:302px;background:linear-gradient(135deg,#1d3a57,#6d8499 50%,#dce3ea)"></div>
<div class="photo" role="img" aria-label="Photo of a lawyer on the phone at her desk" style="left:959px;top:2410px;width:241px;height:302px;background:linear-gradient(135deg,#f0efec,#a6a39f 55%,#2d2c2b)"></div>

<!-- APPOINTMENT -->
<div class="abs" style="left:1023px;top:2837px;width:177px;height:656px;background:var(--rust);clip-path:polygon(0 40px,100% 0,100% 100%,0 100%)"></div>
<div class="eyebrow" style="left:538px;top:2839px;color:var(--ink)">Contact Us</div>
<h2 class="heading" style="left:0;width:1200px;text-align:center;top:2868px">Make An Appointment</h2>
<div class="quote" style="top:2986px"><span class="mark">&ldquo;</span>Lorem Ipsum is simply dummy text of the printing and typesetting industry. Lorem Ipsum has been the industry's standard dummy text ever since the 1500s.</div>
<div class="client" style="top:3076px"><div class="avatar" role="img" aria-label="Client portrait"></div><div><b>Client Name</b><span>- Services</span></div></div>
<div class="quote" style="top:3181px"><span class="mark">&ldquo;</span>Lorem Ipsum is simply dummy text of the printing and typesetting industry. Lorem Ipsum has been the industry's standard dummy text ever since the 1500s.</div>
<div class="client" style="top:3271px"><div class="avatar" role="img" aria-label="Client portrait"></div><div><b>Client Name</b><span>- Services</span></div></div>
<div class="form">
  <h3>Get In Contact With Us !</h3>
  <div class="field" style="left:42px;top:131px;width:218px">Name :</div>
  <div class="field" style="left:274px;top:131px;width:218px">Phone No :</div>
  <div class="field" style="left:42px;top:176px;width:218px">Your Email :</div>
  <div class="field" style="left:274px;top:176px;width:218px">Appointment :</div>
  <div class="field" style="left:42px;top:221px;width:450px;height:90px">Message :</div>
  <div class="btn" style="left:42px;top:342px;width:124px;height:35px;box-shadow:4px 4px 0 -1px #1b1a19,5px 5px 0 0 var(--rust)">SUBMIT NOW</div>
</div>

<!-- NEWS -->
<section class="news"></section>
<div class="eyebrow" style="left:0;width:1200px;justify-content:center;top:3532px;color:#fff"><span style="margin:0">Blog</span></div>
<h2 class="heading" style="left:0;width:1200px;text-align:center;top:3560px">Latest News</h2>
<div class="card" style="left:112px">
  <div class="img" role="img" aria-label="Photo of a lawyer working on a laptop with scales of justice" style="background:linear-gradient(135deg,#e8e6e2,#8c8781 50%,#29303a)"></div>
  <div class="meta"><span><svg width="12" height="12" viewBox="0 0 12 12" fill="none" stroke="#c4620c" stroke-width="1.3"><rect x="1" y="2" width="10" height="9"/><path d="M1 5h10"/></svg>3 Dec, 2021</span><span><svg width="12" height="12" viewBox="0 0 12 12" fill="none" stroke="#c4620c" stroke-width="1.3"><path d="M2 10l5-5M6 2l4 4-2 2-4-4z"/></svg>Attorney</span></div>
  <h4>Lorem Ipsum is simply dummy text of the printing .</h4>
</div>
<div class="card" style="left:444px">
  <div class="img" role="img" aria-label="Photo of a smiling attorney in front of a law library" style="background:linear-gradient(135deg,#5a3a1e,#b58a5a 50%,#3a2a1c)"></div>
  <div class="meta"><span><svg width="12" height="12" viewBox="0 0 12 12" fill="none" stroke="#c4620c" stroke-width="1.3"><rect x="1" y="2" width="10" height="9"/><path d="M1 5h10"/></svg>3 Dec, 2021</span><span><svg width="12" height="12" viewBox="0 0 12 12" fill="none" stroke="#c4620c" stroke-width="1.3"><path d="M2 10l5-5M6 2l4 4-2 2-4-4z"/></svg>Attorney</span></div>
  <h4>Lorem Ipsum is simply dummy text of the printing .</h4>
</div>
<div class="card" style="left:774px">
  <div class="img" role="img" aria-label="Photo of two business people discussing over a laptop" style="background:linear-gradient(135deg,#2a2b2e,#9a9ca0 55%,#e4e5e7)"></div>
  <div class="meta"><span><svg width="12" height="12" viewBox="0 0 12 12" fill="none" stroke="#c4620c" stroke-width="1.3"><rect x="1" y="2" width="10" height="9"/><path d="M1 5h10"/></svg>3 Dec, 2021</span><span><svg width="12" height="12" viewBox="0 0 12 12" fill="none" stroke="#c4620c" stroke-width="1.3"><path d="M2 10l5-5M6 2l4 4-2 2-4-4z"/></svg>Attorney</span></div>
  <h4>Lorem Ipsum is simply dummy text of the printing .</h4>
</div>

<!-- CLIENTS -->
<div class="eyebrow" style="left:518px;top:4057px;color:var(--ink)">Client</div>
<h2 class="heading" style="left:0;width:1200px;text-align:center;top:4086px">Featured Client</h2>
<div class="brand" style="left:135px;font-size:22px"><i></i>Larchway</div>
<div class="brand" style="left:367px"><i></i>Fernhill</div>
<div class="brand" style="left:600px"><i></i>Ridgeline</div>
<div class="brand" style="left:831px"><i></i>Pinecrest</div>

<!-- SUBSCRIBE + FOOTER -->
<section class="footer"></section>
<div class="abs" style="left:150px;top:4323px;width:1008px;height:300px;background:var(--cream)"></div>
<div class="photo" role="img" aria-label="Photo of a lawyer working at a desk with a laptop, books and a justice statue" style="left:150px;top:4323px;width:375px;height:300px;background:linear-gradient(135deg,#d9d6d0,#f3f1ec 40%,#56606e 70%,#c9c3ba)"></div>
<h2 class="serif" style="position:absolute;left:585px;top:4368px;font-weight:700;font-size:26px;line-height:38px;color:var(--rust)">Subscribe Your Email For<br>Newsletter &amp; Promotion</h2>
<div class="abs" style="left:585px;top:4466px;width:382px;height:36px;border:1px solid #d7b08a;background:#fff;font-size:11px;color:#888;padding:11px 10px">Enter Email Address...</div>
<div class="btn" style="left:585px;top:4520px;width:126px;height:36px;box-shadow:4px 4px 0 -1px var(--cream),5px 5px 0 0 var(--rust)">SEND MESSAGE</div>
<div class="photo" role="img" aria-label="Photo of a judge's gavel" style="left:990px;top:4440px;width:170px;height:160px;background:radial-gradient(ellipse at 50% 55%,#6b3b1a,#3a1f0d 50%,rgba(0,0,0,0) 72%)"></div>

<div class="logo" style="left:62px;top:4673px"><span class="l1">Hartwell &amp;</span><span class="l2">Brody P.C.</span></div>
<div class="fcol" style="left:337px"><h5>Site Map</h5><ul><li>- Home</li><li>- About Us</li><li>- Services</li><li>- Attorney</li><li>- Blog</li><li>- Contact Us</li></ul></div>
<div class="fcol" style="left:613px"><h5>Our Services</h5><ul><li>- State governments</li><li>- Industries</li><li>- Law firms</li><li>- Individuals</li></ul></div>
<div class="fcol" style="left:888px;width:240px">
  <h5>Contact Us</h5>
  <div style="display:flex;gap:12px;line-height:20px"><svg width="16" height="18" viewBox="0 0 16 18" fill="none" stroke="#c4620c" stroke-width="1.5" style="flex:none"><path d="M8 17s6-6 6-10A6 6 0 0 0 2 7c0 4 6 10 6 10z"/><circle cx="8" cy="7" r="2"/></svg>101 - Lorem Ipsum is simply dummy text</div>
  <div style="display:flex;gap:12px;margin-top:16px"><svg width="16" height="16" viewBox="0 0 24 24" fill="none" stroke="#c4620c" stroke-width="2"><path d="M5 3h4l2 5-3 2a12 12 0 0 0 6 6l2-3 5 2v4a2 2 0 0 1-2 2A17 17 0 0 1 3 5a2 2 0 0 1 2-2z"/></svg>+1 406 555 0198</div>
  <div style="display:flex;gap:12px;margin-top:38px"><svg width="20" height="14" viewBox="0 0 22 14" fill="none" stroke="#c4620c" stroke-width="1.6"><rect x="1" y="1" width="20" height="12"/><path d="M1 1l10 7 10-7"/></svg>office@hartwellbrody.law</div>
</div>
<div class="copy">©2021 Hartwell &amp; Brody P.C. - All Right Reserved.</div>

</body>
</html>
```